Brisk Pressworks Promotional Brochure

www.briskpressworks.example

Award Winning Trade Printer

Refer to website and create a Brochure 5 colour using metallic gold 871
Images can be supplied hi resolution from website if required or further images

Using the following titles
Specialising in High Quality Trade Printing Nationally
Books, Catalogues, Booklets
Brochures, Flyers and Mail Outs
Presentation Folders
Business Cards and Stationery
Also Specialising in
Labels and Packaging
print and engineering from original concept packaging

Come and see our friendly staff or visit our website
Compare our prices via email

Target Market(s)

Print Buyers

Industry/Entity Type

Printing

Requirements
Must have
• a pms Gold included in final artwork
• A Premium/Quality/upmarket approach
• Hi Quality IMAGES etc.
• I placed an image of an awards dinner BUT that is just there for a personal image not essential to have by any means
Nice to have
• Sections in the brochure for each type of print or panel with a cover page wow!!! BRISK!
Should not have
• poor quality images

```html
<!DOCTYPE html>
<html lang="en">
<head>
<meta charset="utf-8">
<title>Brisk Pressworks Trifold Brochure</title>
<link rel="stylesheet" href="https://fonts.googleapis.com/css2?family=Lato:wght@300;400;700&family=Roboto+Condensed:wght@400&family=Roboto:wght@300&display=swap">
<style>
  :root {
    --backdrop: #3a2a1c;
    --gold-light: #f2c23e;
    --gold: #e3a92a;
    --gold-deep: #c98e1c;
    --navy: #1c1f5e;
    --maroon: #7a1216;
    --maroon-deep: #5a0c0f;
    --stripe-red: #8e1b1f;
    --white: #ffffff;
    --black: #0d0d0d;
    --charcoal: #262626;
    --ink: #1a1a1a;
    --text-light: #e9e9e9;
  }
  * { margin: 0; padding: 0; box-sizing: border-box; }
  html, body { width: 1200px; height: 907px; overflow: hidden; }
  body {
    background: var(--backdrop);
    font-family: "Lato", sans-serif;
    position: relative;
  }
  .brochure {
    position: absolute;
    left: 87px; top: 80px;
    width: 1021px; height: 728px;
    display: flex;
    box-shadow: 0 10px 30px rgba(0,0,0,.5);
  }
  .panel { position: relative; height: 100%; overflow: hidden; }

  /* Left panel */
  .panel--about { width: 350px; background: var(--maroon); }
  .gold-band {
    background: linear-gradient(180deg, var(--gold-light), var(--gold) 50%, var(--gold-deep));
  }
  .about-top { position: absolute; left: 0; top: 0; width: 100%; height: 30px; background: var(--navy); }
  .about-top .gold-band { position: absolute; left: 0; bottom: 0; width: 100%; height: 12px; }
  .photo-awards {
    position: absolute; left: 0; top: 30px; width: 100%; height: 298px;
    background: radial-gradient(ellipse at 55% 55%, #c0392b 0%, #6b2620 28%, #2a1d1a 60%, #141010 100%);
  }
  .about-divider { position: absolute; left: 0; top: 328px; width: 100%; height: 32px; background: var(--navy); }
  .about-divider .gold-band { position: absolute; left: 0; top: 0; width: 100%; height: 12px; }
  .about-body {
    position: absolute; left: 0; top: 360px; width: 100%; height: 292px;
    background: linear-gradient(180deg, var(--maroon-deep), var(--maroon) 45%, #8c1a1d);
    padding: 18px 40px 0 20px;
    color: var(--white);
  }
  .about-title {
    font-family: "Lato", sans-serif; font-weight: 400;
    font-size: 14.5px; color: var(--gold-light); letter-spacing: .3px;
    margin-bottom: 10px;
  }
  .about-body p { font-size: 11px; line-height: 14.4px; }
  .stripes { position: absolute; left: 0; width: 100%; }
  .stripes span { display: block; width: 100%; }
  .stripes .s-white { height: 5px; background: var(--white); }
  .stripes .s-red { height: 5px; background: var(--stripe-red); }
  .about-stripes { top: 655px; }
  .footer-web {
    position: absolute; left: 0; bottom: 0; width: 100%; height: 62px;
    display: flex; align-items: center; justify-content: center;
    font-family: "Roboto Condensed", sans-serif; font-size: 14px;
    letter-spacing: 1.6px; color: var(--ink);
  }

  /* Brand name (plain wordmark placeholder) */
  .brand-name {
    position: absolute;
    font-family: "Lato", sans-serif; font-weight: 400;
    font-size: 30px; color: var(--white);
    text-align: center; width: 100%; left: 0;
  }

  /* Middle panel */
  .panel--contact {
    width: 333px;
    background: linear-gradient(90deg, #0a0a0a, var(--charcoal) 50%, #0a0a0a);
    color: var(--text-light); text-align: center;
  }
  .contact-brand { top: 243px; }
  .contact-details { position: absolute; left: 0; top: 357px; width: 100%; font-size: 14.5px; line-height: 18.5px; }
  .contact-details .address { margin-bottom: 6px; }
  .contact-details .line { margin-bottom: 6.5px; }
  .contact-details .label { color: var(--gold-light); font-weight: 700; }

  /* Right panel */
  .panel--cover { width: 338px; background: linear-gradient(180deg, #111, var(--charcoal) 50%, #111); }
  .cover-top { position: absolute; left: 0; top: 0; width: 100%; height: 48px; }
  .cover-top-stripes { top: 48px; }
  .cover-brand { top: 106px; }
  .cover-photo-frame { position: absolute; left: 0; top: 198px; width: 100%; height: 282px; }
  .cover-photo-frame .gold-band { position: absolute; left: 0; width: 100%; height: 6px; }
  .cover-photo-frame .gold-band.top { top: 0; }
  .cover-photo-frame .gold-band.bottom { bottom: 0; }
  .photo-press {
    position: absolute; left: 0; top: 10px; width: 100%; height: 262px;
    background: linear-gradient(180deg, #d9d9d9 0%, #8c8c8c 35%, #5a5a5a 60%, #1e1e1e 100%);
  }
  .cover-tagline { position: absolute; left: 0; top: 540px; width: 100%; text-align: center; }
  .tagline-kicker {
    font-family: "Roboto Condensed", sans-serif; font-size: 21px;
    color: var(--gold-light); letter-spacing: .3px; line-height: 26px;
  }
  .tagline-main {
    font-family: "Roboto", sans-serif; font-weight: 300;
    font-size: 43px; color: var(--white); line-height: 46px;
  }
  .cover-stripes { top: 655px; }
</style>
</head>
<body>
  <main class="brochure">
    <section class="panel panel--about">
      <div class="about-top"><div class="gold-band"></div></div>
      <div class="photo-awards" role="img" aria-label="Photo of a staff member holding a glass award at an awards dinner"></div>
      <div class="about-divider"><div class="gold-band"></div></div>
      <div class="about-body">
        <h2 class="about-title">ABOUT US</h2>
        <p>Brisk Pressworks takes great pride in our craftsmanship, skill and ingenuity to ensure we deliver the best possible printing outcome for every job.</p>
        <p>Known widely as a ‘printer’s printer’ there is no job too small, large or complex for Brisk Pressworks from your smallest business card run through to the most intricate and difficult printing task.</p>
        <p>Renown for high quality of work, state-of-the-art tech-nology and commitment to excellence, Brisk have worked hard to be established as one of the premier printers in Tasmania.</p>
        <p>Pride and quality drive the efforts of staff to ensure your printing requirements are delivered on–time with professionalism and expertise.</p>
      </div>
      <div class="stripes about-stripes"><span class="s-white"></span><span class="s-red"></span></div>
      <div class="footer-web gold-band">www.briskpressworks.example</div>
    </section>

    <section class="panel panel--contact">
      <p class="brand-name contact-brand">BRISK</p>
      <div class="contact-details">
        <p class="address">18 Ledger Lane<br>Northvale 7100 Tasmania<br>Australia</p>
        <p class="line"><span class="label">Call-</span> 03 5550 1402</p>
        <p class="line"><span class="label">Fax-</span>03 5550 1463</p>
        <p class="line"><span class="label">Email-</span>print@briskpressworks.example</p>
        <p class="line"><span class="label">Visit us-</span>www.briskpressworks.example</p>
      </div>
    </section>

    <section class="panel panel--cover">
      <div class="cover-top gold-band"></div>
      <div class="stripes cover-top-stripes"><span class="s-red"></span><span class="s-white"></span></div>
      <p class="brand-name cover-brand">BRISK</p>
      <div class="cover-photo-frame">
        <div class="gold-band top"></div>
        <div class="photo-press" role="img" aria-label="Black and white photo of an offset printing press with coloured ink rollers"></div>
        <div class="gold-band bottom"></div>
      </div>
      <div class="cover-tagline">
        <p class="tagline-kicker">PRINTING IS MORE THAN A JOB</p>
        <p class="tagline-main">it is an artform</p>
      </div>
      <div class="stripes cover-stripes"><span class="s-white"></span><span class="s-red"></span></div>
      <div class="footer-web gold-band">www.briskpressworks.example</div>
    </section>
  </main>
</body>
</html>
```